Webdesign für Automotive Engineering Webpage
Zielgruppe
Automotive Engineering - Main focus is Software Development & Embedded systems for the Automotive industry.
Like as HMI, ADAS, ECU
Aufgabenstellung
See Logo (PDF), example --> https://www.trelvona.com/de/de (competetor)

```html
<!DOCTYPE html>
<html lang="de">
<head>
<meta charset="utf-8">
<title>VERANTEC – Die Nr. 1 in Engineering</title>
<link rel="stylesheet" href="https://fonts.googleapis.com/css2?family=Bebas+Neue&family=Open+Sans:wght@300;400;600;700&display=swap">
<style>
:root{
  --navy:#161c2c;
  --navy-deep:#111727;
  --panel:#252c3c;
  --card:#1f2636;
  --red:#e4161f;
  --ice:#eff4fc;
  --text:#3a3f4a;
  --muted:#8a92a3;
  --line:#d5dcea;
  --white:#ffffff;
}
*{box-sizing:border-box;margin:0;padding:0}
html,body{width:1200px;height:3152px;overflow:hidden;background:var(--white)}
body{position:relative;font-family:"Open Sans",sans-serif;color:var(--text)}
.abs{position:absolute}
.display{font-family:"Bebas Neue",sans-serif;letter-spacing:.5px}

/* hero */
.hero{left:0;top:0;width:1200px;height:834px;background:linear-gradient(180deg,var(--navy) 0%,#1a2133 100%)}
.hero-panel{left:0;top:0;width:339px;height:834px;background:linear-gradient(180deg,#2a3142 0%,#222a3b 100%)}
.brand{left:32px;top:32px;color:var(--white);font-weight:700;font-size:14px;letter-spacing:1px;display:flex;align-items:center;gap:6px}
.brand-dot{width:8px;height:8px;background:var(--red);border-radius:50%}
.nav{top:32px;font-size:11px;font-weight:700;color:var(--white);letter-spacing:.3px}
.nav span{position:absolute;white-space:nowrap}
.menu-btn{left:1133px;top:0;width:67px;height:67px;background:var(--red)}
.follow{left:30px;top:148px;color:#aab2c2;font-size:8px;font-weight:700;writing-mode:vertical-rl;letter-spacing:.5px}
.follow-line{left:39px;top:200px;width:1px;height:137px;background:#5b6475}
.social{left:33px;width:12px;height:12px;border-radius:50%;background:#c4cbd8}
.hero-visual{left:110px;top:238px;width:446px;height:153px;border-radius:60px 120px 30px 30px;background:radial-gradient(ellipse at 50% 55%,#5d6270 0%,#3a3f4c 55%,rgba(34,42,59,0) 75%)}
.hero-title{left:643px;top:218px;font-size:54px;color:#dfe3ec;white-space:nowrap}
.hero-title em{font-style:normal;color:var(--red)}
.hero-sub{left:643px;top:286px;font-size:13.5px;line-height:19px;color:#a0a8b8;width:300px}
.btn{background:var(--red);color:var(--white);font-size:11px;font-weight:700;border-radius:14px;display:flex;align-items:center;justify-content:center}
.hero-btn{left:643px;top:356px;width:130px;height:23px}
.services{left:133px;top:550px;width:933px;height:233px;background:rgba(40,48,66,.75);border-radius:6px}
.service{top:0;width:300px;height:233px;text-align:center}
.service svg{position:absolute;top:58px;left:132px}
.service h3{position:absolute;top:126px;width:100%;font-family:"Bebas Neue",sans-serif;font-size:20px;color:#e6e9ef;font-weight:400}
.service p{position:absolute;top:162px;width:100%;font-size:13px;line-height:18px;color:#8a92a3}

/* vertical section labels */
.side-label{transform:rotate(-90deg);transform-origin:0 0;white-space:nowrap;color:#1f2433;font-size:30px;line-height:33px}
.side-label .light{display:block;font-weight:300}
.side-label .bold{display:block;font-weight:700}

/* leistungen */
.tab{top:934px;font-family:"Bebas Neue",sans-serif;font-size:20px;display:flex;align-items:center;gap:12px;white-space:nowrap}
.tab-active{color:#1f2433}
.tab-idle{color:#b4bfd2}
.tab-bar{left:229px;top:976px;width:268px;height:4px;background:var(--red)}
.content-box{left:229px;top:981px;width:838px;height:325px;background:var(--ice);padding:33px 34px;font-size:13.5px;line-height:20px}
.content-box p{margin-bottom:20px}
.content-box strong{font-weight:700;color:#262b36}

/* ueber uns */
.rule{left:0;width:827px;height:1px;background:var(--line)}
.about-shape{left:872px;top:1429px;width:195px;height:479px;background:var(--ice);border-radius:240px 0 0 240px}
.about-visual{left:742px;top:1517px;width:383px;height:318px;border-radius:46% 52% 40% 44%;background:radial-gradient(ellipse at 45% 40%,#ffffff 0%,#e3e7ee 45%,#7d8799 75%,#3c4456 100%)}
.kicker{font-size:31px;font-weight:300;color:#1f2433;line-height:1.1}
.heading{font-size:31px;font-weight:700;color:#1f2433;line-height:1.1}
.about-head{left:133px;top:1470px}
.about-text{left:133px;top:1563px;width:560px;font-size:13.5px;line-height:20px}
.about-text p{margin-bottom:20px}

/* blog */
.arrow{top:2010px;width:45px;height:45px;background:#c3cfe0;display:flex;align-items:center;justify-content:center}
.blog-clip{left:229px;top:2060px;width:838px;height:520px;overflow:hidden}
.post{top:0;width:300px;text-align:center}
.post-img{width:300px;height:250px}
.post h4{margin-top:26px;font-family:"Bebas Neue",sans-serif;font-weight:400;font-size:20px;color:#1f2433;white-space:nowrap}
.post p{margin:10px 34px 0;font-size:13.5px;line-height:18.5px;color:#3a3f4a}
.post .more{display:block;margin-top:26px;font-size:11px;font-weight:700;color:var(--red)}
.post .post-rule{margin-top:28px;height:1px;background:#3d4d74}

/* footer */
.footer{left:0;top:2676px;width:1200px;height:476px;background:linear-gradient(180deg,#1a2133 0%,var(--navy-deep) 100%)}
.f-kicker{font-size:20px;font-weight:300;color:#d8dde7;line-height:1.3}
.f-heading{font-size:20px;font-weight:700;color:var(--white);line-height:1.3}
.f-brand{left:133px;top:2840px;color:var(--white);font-size:28px;font-weight:700;letter-spacing:1px;display:flex;align-items:center;gap:8px}
.f-brand i{width:10px;height:10px;background:var(--red);border-radius:50%;display:block}
.f-line{left:170px;font-size:11.5px;line-height:16px;color:#d4d9e3}
.field{left:450px;width:617px;height:23px;border:1px solid var(--red);border-radius:12px;font-size:11.5px;color:#c9cfdb;padding:3px 11px}
.send{left:450px;top:2997px;width:83px;height:24px;font-size:11.5px}
.legal{top:3120px;font-size:11px;color:#c6ccd8;white-space:nowrap}
</style>
</head>
<body>

<!-- HERO -->
<section class="abs hero"></section>
<div class="abs hero-panel"></div>
<div class="abs brand"><span class="brand-dot"></span>VERANTEC</div>
<nav class="abs nav" style="left:0;width:1200px">
  <span style="left:692px">HOME</span>
  <span style="left:769px">LEISTUNGEN</span>
  <span style="left:884px">ÜBER UNS</span>
  <span style="left:992px">KONTAKT US</span>
</nav>
<div class="abs menu-btn">
  <svg width="67" height="67" viewBox="0 0 67 67"><g stroke="#fff" stroke-width="2" stroke-linecap="round"><line x1="22" y1="27" x2="46" y2="27"/><line x1="28" y1="33" x2="46" y2="33"/><line x1="22" y1="39" x2="46" y2="39"/></g></svg>
</div>
<div class="abs follow">FOLLOW US</div>
<div class="abs follow-line"></div>
<div class="abs social" style="top:369px"></div>
<div class="abs social" style="top:403px"></div>
<div class="abs social" style="top:436px"></div>
<div class="abs social" style="top:471px"></div>
<div class="abs hero-visual" role="img" aria-label="Dunkelgrauer Supersportwagen in Seitenansicht"></div>
<h1 class="abs hero-title display">DIE <em>NR. 1</em> IN ENGINEERING</h1>
<p class="abs hero-sub">Beste internationale fahrzeugtechnische Dienstleistungen für das Engineering</p>
<a class="abs btn hero-btn">LEARN MORE</a>

<div class="abs services">
  <div class="abs service" style="left:0">
    <svg width="40" height="40" viewBox="0 0 40 40" fill="none" stroke="#e4161f" stroke-width="2"><circle cx="20" cy="20" r="6"/><path d="M20 3l3 5 6-2 1 6 6 1-2 6 5 3-5 3 2 6-6 1-1 6-6-2-3 5-3-5-6 2-1-6-6-1 2-6-5-3 5-3-2-6 6-1 1-6 6 2z"/></svg>
    <h3>FULL SERVICE ENGINEERING</h3>
    <p>Übernahme Kompletter R&amp;D Projekte<br>Als Fremdleistung</p>
  </div>
  <div class="abs service" style="left:316px">
    <svg width="40" height="40" viewBox="0 0 40 40" fill="none" stroke="#e4161f" stroke-width="2"><rect x="3" y="11" width="34" height="24" rx="3"/><path d="M14 11V6h12v5M12 11v24M28 11v24"/></svg>
    <h3>PREMIUM RECRUITING</h3>
    <p>Vermittlung Bis Hin Zum Onboarding<br>Von Freelancern Und Festangestellten</p>
  </div>
  <div class="abs service" style="left:633px">
    <svg width="40" height="40" viewBox="0 0 40 40" fill="none" stroke="#e4161f" stroke-width="2"><circle cx="15" cy="12" r="6"/><path d="M3 34c0-7 5-11 12-11s12 4 12 11"/><path d="M25 6a6 6 0 010 12M30 23c4 2 7 6 7 11"/></svg>
    <h3>TEMPING</h3>
    <p>Automotive R&amp;D Experten und<br>Ingenieure in Zeitarbeit</p>
  </div>
</div>

<!-- LEISTUNGEN -->
<div class="abs side-label" style="left:135px;top:1163px"><span class="light">UNSER</span><span class="bold">LEISTUNGEN</span></div>
<div class="abs tab tab-active" style="left:259px">
  <svg width="22" height="22" viewBox="0 0 40 40" fill="none" stroke="#e4161f" stroke-width="2.5"><circle cx="20" cy="20" r="6"/><path d="M20 3l3 5 6-2 1 6 6 1-2 6 5 3-5 3 2 6-6 1-1 6-6-2-3 5-3-5-6 2-1-6-6-1 2-6-5-3 5-3-2-6 6-1 1-6 6 2z"/></svg>FULL SERVICE ENGINEERING</div>
<div class="abs tab tab-idle" style="left:559px">
  <svg width="22" height="22" viewBox="0 0 40 40" fill="none" stroke="#b4bfd2" stroke-width="2.5"><rect x="3" y="11" width="34" height="24" rx="3"/><path d="M14 11V6h12v5M12 11v24M28 11v24"/></svg>PREMIUM RECRUITING</div>
<div class="abs tab tab-idle" style="left:884px">
  <svg width="22" height="22" viewBox="0 0 40 40" fill="none" stroke="#b4bfd2" stroke-width="2.5"><circle cx="15" cy="12" r="6"/><path d="M3 34c0-7 5-11 12-11s12 4 12 11"/><path d="M25 6a6 6 0 010 12M30 23c4 2 7 6 7 11"/></svg>TEMPING</div>
<div class="abs tab-bar"></div>
<div class="abs content-box">
  <p>Neben der Entlastung bei Bedarfsspitzen und der Direktvermittlung von Vakanzen übernehmen wir auch Ihre Projekte komplett als Fremdleistung. Sie übergeben uns Ihre Aufgaben, wir liefern Ihnen das Ergebnis – pünktlich und qualitativ hochwertig!</p>
  <p><strong>Unsere Teams beherrschen unter anderem die Sparten</strong><br>
  • E-Mobilität / Elektrifizierung<br>
  • Autonomes Fahren<br>
  • Fahrassistenzsysteme, ADAS<br>
  • Prototypen / Testing<br>
  • Prozessoptimierung in der Produktentwicklung<br>
  • Projektmanagement</p>
  <p><strong>Bei uns finden Sie die Ressourcen, die Ihnen fehlen</strong></p>
</div>

<!-- UEBER UNS -->
<div class="abs rule" style="top:1429px"></div>
<div class="abs rule" style="top:1908px"></div>
<div class="abs about-shape"></div>
<div class="abs about-visual" role="img" aria-label="Weißes futuristisches Einrad-Fahrzeug mit Glaskuppel"></div>
<div class="abs about-head"><div class="kicker">UBER UNS</div><div class="heading">WER WIR SIND</div></div>
<div class="abs about-text">
  <p>Hallberg Recruitment vereint in sich 25 Jahre Branchen- und Projekterfahrung vom Freelance Ingenieur bis zum Task Force Manager in den Branchen Automotive, Schienenfahrzeuge, Luft- und Raumfahrt, Rüstung und Informationstechnologie.</p>
  <p>Firmengründer und Geschäftsführer Lukas Hallberg kennt die Industrie seit über zwei Jahrzehnten, in denen er in Positionen als IT Entwicklungsingenieur, Experte für Geodaten und rund um das Thema autonomes Fahren und Fahrassistenzsysteme, bis zum CIO und Task Force Manager bei fast allen wichtigen OEMs und Tier1s des Automotive Sektors und anderer Schlüsselindustrien Erfahrungen sammeln konnte.</p>
  <p>Wie der Firmengründer, so verfügen auch alle maßgeblichen Mitarbeiter bei Hallberg Recruitment über diese Double Qualification – wir sprechen Ihre Sprache und wissen, wo Ihr Bedarf liegt, kennen Ihre Abläufe und Prozesse, sind aus eigener Erfahrung heraus im Geschäft.</p>
</div>

<!-- BLOG -->
<div class="abs side-label" style="left:135px;top:2338px"><span class="light">UNSER BLOG</span><span class="bold">LESEN SIE TECHNIK</span></div>
<div class="abs arrow" style="left:229px"><svg width="14" height="20" viewBox="0 0 14 20"><path d="M10 3L3 10l7 7" fill="none" stroke="#fff" stroke-width="2.5"/></svg></div>
<div class="abs arrow" style="left:279px"><svg width="14" height="20" viewBox="0 0 14 20"><path d="M4 3l7 7-7 7" fill="none" stroke="#fff" stroke-width="2.5"/></svg></div>
<div class="abs blog-clip">
  <article class="abs post" style="left:0">
    <div class="post-img" role="img" aria-label="Motorraum mit Rohren und Bauteilen in Blautönen" style="background:linear-gradient(135deg,#4a5a78,#1c2436)"></div>
    <h4>IRRWITZ IM WECKER</h4>
    <p>Lorem ipsum dolor sit amet, consectetur adipiscing elit. Sodales adipiscing eget iaculis amet morbi. Egestas ipsum massa dolor gravida. A mattis viverra et malesuada mollis rhoncus tincidunt. Ante suspendisse sed risus est vitae convallis felis.</p>
    <span class="more">WEITERLESEN ›</span>
    <div class="post-rule"></div>
  </article>
  <article class="abs post" style="left:334px">
    <div class="post-img" role="img" aria-label="Beleuchteter Drehzahlmesser im dunklen Cockpit" style="background:radial-gradient(ellipse at 50% 80%,#3a1a1a,#0a0c14 70%)"></div>
    <h4>LICHT AM ENDE DES TUNNELS</h4>
    <p>Lorem ipsum dolor sit amet, consectetur adipiscing elit. Sodales adipiscing eget iaculis amet morbi. Egestas ipsum massa dolor gravida. A mattis viverra et malesuada mollis rhoncus tincidunt. Ante suspendisse sed risus est vitae convallis felis.</p>
    <span class="more">WEITERLESEN ›</span>
    <div class="post-rule"></div>
  </article>
  <article class="abs post" style="left:667px">
    <div class="post-img" role="img" aria-label="Nahaufnahme eines Motorblocks" style="background:linear-gradient(135deg,#2d3a55,#6b6a5a)"></div>
    <h4>JETZT IST AGILITÄT GEFRAGT</h4>
    <p>Lorem ipsum dolor sit amet, consectetur adipiscing elit. Sodales adipiscing eget iaculis amet morbi. Egestas ipsum massa dolor gravida. A mattis viverra et malesuada mollis rhoncus tincidunt. Ante suspendisse sed risus est vitae convallis felis.</p>
    <span class="more">WEITERLESEN ›</span>
    <div class="post-rule"></div>
  </article>
</div>

<!-- FOOTER -->
<footer class="abs footer"></footer>
<div class="abs" style="left:133px;top:2749px"><div class="f-kicker">ADDRESS &amp; CONTACT</div><div class="f-heading">VERANTEC GmbH</div></div>
<div class="abs" style="left:450px;top:2749px"><div class="f-kicker">SUCHEN SIE SPEZIALISTEN?</div><div class="f-heading">KONTAKTIERE UNS JETZT</div></div>
<div class="abs f-brand"><i></i>VERANTEC</div>
<svg class="abs" style="left:133px;top:2910px" width="20" height="26" viewBox="0 0 20 26"><path d="M10 1C5 1 1.5 4.5 1.5 9.5 1.5 16 10 25 10 25s8.5-9 8.5-15.5C18.5 4.5 15 1 10 1z" fill="none" stroke="#e4161f" stroke-width="1.8"/><circle cx="10" cy="9.5" r="3" fill="none" stroke="#e4161f" stroke-width="1.8"/></svg>
<div class="abs f-line" style="top:2906px">Lindenstraße 24<br>D - 34560 Waldbrunn OT Oberau</div>
<div class="abs f-line" style="top:2960px">+49 (0)5600 - 123 45 67</div>
<svg class="abs" style="left:132px;top:2994px" width="24" height="18" viewBox="0 0 24 18"><rect x="1" y="1" width="22" height="16" rx="2" fill="none" stroke="#e4161f" stroke-width="1.8"/><path d="M1 2l11 8 11-8" fill="none" stroke="#e4161f" stroke-width="1.8"/></svg>
<div class="abs f-line" style="top:2995px">office@hallberg-recruitment.de</div>

<div class="abs field" style="top:2830px">Name</div>
<div class="abs field" style="top:2872px">Deine E-Mail</div>
<div class="abs field" style="top:2914px">Telefonnummer</div>
<div class="abs field" style="top:2955px">Ort/PLZ</div>
<a class="abs btn send">SENDEN</a>

<div class="abs legal" style="left:128px">© VERANTEC GMBH 2020</div>
<div class="abs legal" style="left:713px">KONTAKT</div>
<div class="abs legal" style="left:807px">AGB</div>
<div class="abs legal" style="left:873px">IMPRESSUM</div>
<div class="abs legal" style="left:982px">DATENSCHUTZ</div>

</body>
</html>
```